Trucking Insurance Website Design

We are working with a Trucking Insurance company in California. They provide vehicle insurance for trucking companies and truckers.
As you might imagine, there are no websites we could find for inspiration for trucking insurance. But below are sites that do similar insurance.
https://brindlemorecover.com/trucking-insurance/
https://www.haulwardpolicy.com/california-commercial-truck-insurance
Thank you for taking the time to consider designing a website for us. We are web developers based in Stockton, CA, USA. Most of our projects go through the same process. Understanding this process may help you win a project with us. We custom-code all of our websites in-house. We don’t have any requirements as to what tools you use for your design, but we ask that you follow these guidelines.
IMAGES:
If you use any images or icons in the design, we ask that you have a link to the asset so we can purchase the image/icon. Most of the designs we submit do not have the customer’s images on them unless they have some great images. Be creative; show us the feeling you are trying to portray with your image choices. Use any royalty-free site you choose. We subscribe to Quillen and mainly use their images, but we can purchase images outside of Quillen. PLEASE NOTE: we will not submit designs to clients with watermarks on the images.
FONTS:
We ask that you identify the fonts you’re using in the design. This can be done in a message if you want. We typically use Marlowe Type and Quillen Type.
CONTENT:
We're always open to different content and ideas. We often submit designs with stock images so the client can see our vision. We typically take pictures after the website launch to use their images with our vision. Lorem Ipsum is fine for paragraphs, but we ask that you make the Headers with correct English. We want to be able to show the vision and identify the sections of the website.
INSPIRATION:
We typically add a couple of links in the brief of websites we like to help you get started in your design.
REVISIONS:
We do not often ask for revisions of the designs unless we see something in the design that may not appeal to the client. If there are slight changes that we want to make, we do that in the development process.
FEEDBACK:
We rarely give feedback on designs during the design process. We are working on many website projects and do not have the time to provide feedback. We usually respond if your request is well thought out and asks specific questions, but a note asking “feedback, please” usually goes unanswered.
1 page

```html
<!DOCTYPE html>
<html lang="en">
<head>
<meta charset="utf-8">
<title>Ridgeline Cover — Trucking Insurance</title>
<link href="https://fonts.googleapis.com/css2?family=Montserrat:wght@400;500;600;700;800&display=swap" rel="stylesheet">
<style>
:root{
  --blue:#4557c0;
  --red:#d0021b;
  --ink:#1d1d1d;
  --text:#8a8a8a;
  --band:#f0f0f0;
  --footer:#e4e4e4;
  --dark:#1a1a1a;
  --white:#ffffff;
}
*{margin:0;padding:0;box-sizing:border-box}
html,body{width:1200px;height:4630px;overflow:hidden}
body{position:relative;background:var(--white);font-family:"Montserrat",Arial,sans-serif;color:var(--ink)}
.abs{position:absolute}
.btn{position:absolute;display:flex;align-items:center;justify-content:center;background:var(--blue);color:var(--white);font-size:14px;font-weight:600;border-radius:5px}
.brand{position:absolute;display:flex;align-items:center;gap:10px;font-weight:700;color:var(--blue);font-size:17px;letter-spacing:.5px}
.brand .dot{width:22px;height:22px;border-radius:50%;background:var(--red)}
.para{position:absolute;font-size:13.5px;line-height:1.45;color:var(--text)}
.center{text-align:center}
.sec-title{position:absolute;left:0;width:1200px;text-align:center;font-size:36px;font-weight:600;color:var(--ink)}
.sec-title span{color:var(--red)}
/* nav */
.nav{position:absolute;top:52px;left:504px;display:flex;gap:22px;font-size:13px;color:var(--white)}
.nav a{color:var(--white);text-decoration:none}
.nav a.active{color:var(--red)}
.apply{position:absolute;left:984px;top:34px;width:140px;height:54px;background:var(--red);color:var(--white);font-weight:700;font-size:14px;display:flex;align-items:center;justify-content:center;border-radius:4px}
.hero-title{position:absolute;left:74px;top:192px;font-size:53px;font-weight:800;line-height:1.03;color:var(--blue);letter-spacing:.5px}
/* services */
.services{position:absolute;left:5px;top:1291px;width:1195px;height:735px;background:var(--band)}
.card{position:absolute;width:293px;height:217px;background:var(--white);box-shadow:0 2px 8px rgba(0,0,0,.12);text-align:center}
.card .icon{width:60px;height:60px;border-radius:50%;background:#ececec;margin:20px auto 0;display:flex;align-items:center;justify-content:center}
.card h3{font-size:15px;font-weight:600;color:var(--blue);margin-top:22px}
.card p{font-size:12px;line-height:1.6;color:var(--text);margin:10px 22px 0}
.card .more{font-size:14px;font-weight:600;color:#444;margin-top:14px}
.center-brand{position:absolute;left:463px;top:1604px;width:277px;height:278px;display:flex;align-items:center;justify-content:center;font-size:30px;font-weight:700;color:var(--blue);text-align:center;line-height:1.2}
/* business */
.biz{position:absolute;top:2258px;width:326px;height:444px;background:var(--red);border-radius:4px;overflow:hidden}
.biz .photo{height:248px}
.biz h3{color:var(--white);font-size:17px;font-weight:700;margin:36px 22px 0}
.biz p{color:var(--white);font-size:11.5px;line-height:1.7;margin:10px 22px 0}
/* personal */
.personal-bg{position:absolute;left:0;top:2795px;width:1200px;height:562px}
.personal-box{position:absolute;left:241px;top:2935px;width:718px;height:284px;background:rgba(26,26,26,.88)}
/* reasons */
.reasons{position:absolute;left:74px;top:3522px;width:1050px;height:456px;background:#181818;border-radius:4px}
.acc-open{position:absolute;left:68px;top:49px;width:914px;height:41px;background:var(--white);border-radius:4px;display:flex;align-items:center;justify-content:space-between;padding:0 22px;font-size:13px;color:var(--text)}
.acc-answer{position:absolute;left:91px;top:106px;width:460px;font-size:12.5px;line-height:1.55;color:var(--white)}
.acc-item{position:absolute;left:68px;width:914px;height:42px;border-bottom:1px solid #555;display:flex;align-items:center;justify-content:space-between;padding:0 22px;font-size:13px;color:var(--white)}
/* footer */
.footer{position:absolute;left:0;top:4074px;width:1200px;height:484px;background:var(--footer)}
.foot-col{position:absolute;top:138px}
.foot-col h4{font-size:17px;font-weight:500;color:var(--blue)}
.foot-col ul{list-style:none;margin-top:22px;font-size:12px;color:var(--text);line-height:1.65}
.news{position:absolute;left:887px;top:185px;width:237px;height:46px;border:1px solid #9a9a9a;display:flex;align-items:center;justify-content:space-between;padding:0 16px;font-size:12px;color:var(--text)}
.copy{position:absolute;left:0;top:4558px;width:1200px;height:72px;background:var(--dark);color:var(--white);font-size:14px;display:flex;align-items:center;justify-content:center}
</style>
</head>
<body>

<!-- header / hero -->
<svg class="abs" style="left:0;top:0" width="1200" height="660" aria-hidden="false">
  <defs>
    <linearGradient id="sky" x1="0" y1="0" x2="0" y2="1">
      <stop offset="0" stop-color="#7f93d6"/>
      <stop offset=".35" stop-color="#e6a9c6"/>
      <stop offset=".6" stop-color="#c9cbe0"/>
      <stop offset="1" stop-color="#5d5f6e"/>
    </linearGradient>
  </defs>
  <g role="img" aria-label="White semi truck driving on a highway under a pink and blue sunset sky">
    <circle cx="1006" cy="198" r="458" fill="url(#sky)"/>
  </g>
</svg>

<div class="brand" style="left:80px;top:40px"><span class="dot"></span>Ridgeline Cover</div>

<nav class="nav">
  <a class="active" href="#">Home</a>
  <a href="#">About us</a>
  <a href="#">Services</a>
  <a href="#">Business</a>
  <a href="#">Personal</a>
  <a href="#">Contact</a>
</nav>
<div class="apply">Apply Now</div>

<h1 class="hero-title">WELCOME TO<br>RIDGELINE<br>COVER</h1>
<p class="para" style="left:74px;top:396px;width:465px">Lorem Ipsum is simply dummy text of the printing and typesetting industry. Lorem Ipsum has been the industry's standard dummy text ever since the 1500s, when an unknown printer took a galley of type and scrambled it to make a type specimen book.</p>
<div class="btn" style="left:74px;top:516px;width:144px;height:54px">Learn More</div>

<!-- about -->
<div class="abs" role="img" aria-label="Yellow road train truck on an outback highway under a cloudy sky" style="left:74px;top:751px;width:530px;height:460px;background:linear-gradient(180deg,#6f95c4 0%,#c3cfdd 55%,#8d8a78 75%,#4d4d4f 100%)"></div>
<h2 class="abs" style="left:675px;top:846px;font-size:36px;font-weight:600">
  <span style="color:var(--red)">About</span> us</h2>
<p class="para" style="left:675px;top:900px;width:455px">Lorem Ipsum is simply dummy text of the printing and typesetting industry. Lorem Ipsum has been the industry's standard dummy text ever since the 1500s.Lorem Ipsum is simply dummy text of the printing and typesetting industry. Lorem Ipsum has been the industry's standard dummy text ever since the 1500s.</p>
<div class="btn" style="left:675px;top:1038px;width:144px;height:56px">Read More</div>

<!-- services -->
<section class="services"></section>
<h2 class="sec-title" style="top:1355px"><span>Our</span> Services</h2>
<p class="para center" style="left:375px;top:1410px;width:450px">Lorem Ipsum is simply dummy text of the printing and typesetting industry. Lorem Ipsum has been the industry's standard dummy text ever since the 1500s.</p>

<div class="card" style="left:75px;top:1505px">
  <div class="icon"><svg width="26" height="26" viewBox="0 0 26 26" fill="none" stroke="#555" stroke-width="1.6"><circle cx="13" cy="8" r="4"/><path d="M5 22c0-5 4-8 8-8s8 3 8 8"/></svg></div>
  <h3>Trucking Insurance Family</h3>
  <p>Lorem Ipsum is simply dummy text of the printing and typesetting industry.</p>
  <div class="more">Read More</div>
</div>
<div class="card" style="left:75px;top:1744px">
  <div class="icon"><svg width="26" height="26" viewBox="0 0 26 26" fill="none" stroke="#555" stroke-width="1.6"><path d="M13 3l8 3v7c0 5-4 8-8 10-4-2-8-5-8-10V6z"/></svg></div>
  <h3>Trucking Insurance Family</h3>
  <p>Lorem Ipsum is simply dummy text of the printing and typesetting industry.</p>
  <div class="more">Read More</div>
</div>
<div class="card" style="left:830px;top:1505px">
  <div class="icon"><svg width="26" height="26" viewBox="0 0 26 26" fill="none" stroke="#555" stroke-width="1.6"><rect x="5" y="5" width="16" height="16" rx="2"/><path d="M9 13h8M13 9v8"/></svg></div>
  <h3>Trucking Insurance Family</h3>
  <p>Lorem Ipsum is simply dummy text of the printing and typesetting industry.</p>
  <div class="more">Read More</div>
</div>
<div class="card" style="left:830px;top:1744px">
  <div class="icon"><svg width="26" height="26" viewBox="0 0 26 26" fill="none" stroke="#555" stroke-width="1.6"><circle cx="13" cy="13" r="9"/><path d="M8 13l3 3 7-7"/></svg></div>
  <h3>Trucking Insurance Family</h3>
  <p>Lorem Ipsum is simply dummy text of the printing and typesetting industry.</p>
  <div class="more">Read More</div>
</div>
<div class="center-brand">Ridgeline<br>Cover</div>

<!-- business -->
<h2 class="sec-title" style="top:2104px"><span>Our</span> Business</h2>
<p class="para center" style="left:375px;top:2158px;width:450px">Lorem Ipsum is simply dummy text of the printing and typesetting industry. Lorem Ipsum has been the industry's standard dummy text ever since the 1500s.</p>

<article class="biz" style="left:74px">
  <div class="photo" role="img" aria-label="Aerial view of shipping containers in a freight yard" style="background:linear-gradient(160deg,#7a7f83,#a7a59c 50%,#5f6a70)"></div>
  <h3>THE NEXT STEP IS EASY</h3>
  <p>Lorem Ipsum is simply dummy text of the printing and typesetting industry. Lorem Ipsum has been the industry's standard dummy text ever since the 1500s.</p>
</article>
<article class="biz" style="left:438px">
  <div class="photo" role="img" aria-label="Tanker trucks parked on a dirt lot under a blue sky" style="background:linear-gradient(180deg,#2f7fc8,#a8c9e6 55%,#a5715a)"></div>
  <h3>THE NEXT STEP IS EASY</h3>
  <p>Lorem Ipsum is simply dummy text of the printing and typesetting industry. Lorem Ipsum has been the industry's standard dummy text ever since the 1500s.</p>
</article>
<article class="biz" style="left:799px">
  <div class="photo" role="img" aria-label="White delivery lorry parked by a road" style="background:linear-gradient(180deg,#b9c0c4,#e7e7e7 50%,#6b7a5d)"></div>
  <h3>THE NEXT STEP IS EASY</h3>
  <p>Lorem Ipsum is simply dummy text of the printing and typesetting industry. Lorem Ipsum has been the industry's standard dummy text ever since the 1500s.</p>
</article>

<!-- personal -->
<div class="personal-bg" role="img" aria-label="Dark truck on a desert road at dusk with dunes behind" style="background:linear-gradient(180deg,#6b7684 0%,#a3a6a6 45%,#9c8567 72%,#3e3a36 100%)"></div>
<div class="personal-box"></div>
<h2 class="sec-title" style="top:2958px;color:var(--white)"><span>Personal</span> Work</h2>
<p class="para center" style="left:375px;top:3024px;width:450px;color:var(--white)">Lorem Ipsum is simply dummy text of the printing and typesetting industry. Lorem Ipsum has been the industry's standard dummy text ever since the 1500s.</p>
<div class="btn" style="left:528px;top:3132px;width:142px;height:55px">Read More</div>

<!-- reasons -->
<h2 class="sec-title" style="top:3438px"><span>Top</span> Reasons</h2>
<section class="reasons">
  <div class="acc-open">Lorem Ipsum is simply dummy text of.
    <svg width="16" height="10" viewBox="0 0 16 10" fill="none" stroke="#222" stroke-width="2"><path d="M2 2l6 6 6-6"/></svg></div>
  <p class="acc-answer">Lorem Ipsum is simply dummy text of the printing and typesetting industry. Lorem Ipsum has been the industry's standard dummy text ever since the 1500s.</p>
  <div class="acc-item" style="top:192px">Lorem Ipsum is simply dummy text of.<svg width="16" height="10" viewBox="0 0 16 10" fill="none" stroke="#fff" stroke-width="2"><path d="M2 2l6 6 6-6"/></svg></div>
  <div class="acc-item" style="top:253px">Lorem Ipsum is simply dummy text of.<svg width="16" height="10" viewBox="0 0 16 10" fill="none" stroke="#fff" stroke-width="2"><path d="M2 2l6 6 6-6"/></svg></div>
  <div class="acc-item" style="top:312px">Lorem Ipsum is simply dummy text of.<svg width="16" height="10" viewBox="0 0 16 10" fill="none" stroke="#fff" stroke-width="2"><path d="M2 2l6 6 6-6"/></svg></div>
  <div class="acc-item" style="top:371px">Lorem Ipsum is simply dummy text of.<svg width="16" height="10" viewBox="0 0 16 10" fill="none" stroke="#fff" stroke-width="2"><path d="M2 2l6 6 6-6"/></svg></div>
</section>

<!-- footer -->
<footer class="footer">
  <div class="brand" style="left:74px;top:118px"><span class="dot"></span>Ridgeline Cover</div>
  <p class="para" style="left:74px;top:237px;width:255px;font-size:12px">Lorem Ipsum is simply dummy text of the printing and typesetting industry. Lorem Ipsum has been the industry's standard dummy text ever since the 1500s.</p>
  <div class="foot-col" style="left:451px"><h4>About us</h4><ul><li>Home</li><li>About ua</li><li>Services</li><li>Blog</li></ul></div>
  <div class="foot-col" style="left:641px"><h4>Information</h4><ul><li>privacy Policy</li><li>Terms</li><li>Contact us</li></ul></div>
  <div class="foot-col" style="left:887px"><h4>Newsletter</h4></div>
  <div class="news">Email
    <svg width="20" height="18" viewBox="0 0 20 18" fill="none" stroke="#555" stroke-width="1.4"><path d="M1 8l18-7-6 16-3-7z M10 10l9-9"/></svg></div>
</footer>
<div class="copy">Copyright Reserved @ 2023</div>

</body>
</html>
```